Guidance in Calm Posture Support Methods

We need a design/template for an e-learning course. The course is being created for healthcare professionals. The template should include a home page (title), and subtitle page (introduction, chapter, test, help, references and so on). We would like to see designs that are very professional and appealling.

Target Market(s)

Healthcare professionals

Industry/Entity Type

Health Care

Number of Pages Required

4 page

Font styles to use
Sans Serif

Colors
3276b5
85acd3
ffc214
f37122
ffcf3e
886aae
acd136

Requirements
Must have
• The project's title page should be very professional and appealing for a very serious audience. The title page should include an image of healthcare provider, and/or no smoking symbol.
Nice to have
• Pages should include icons such as next and previous buttons, along with progress status bar on bottom of design. Also should include top row containing for primary chapters. In addition, left side of page should contain space for detailed table of contents and additional resources.
Should not have
• Design should not appear cluttered or confusing. Large space for logo.

```html
<!DOCTYPE html>
<html lang="en">
<head>
<meta charset="utf-8">
<title>Guidance in Calm Posture Support Methods</title>
<link href="https://fonts.googleapis.com/css2?family=Montserrat:wght@400;500;600&family=Mulish:wght@400;600&display=swap" rel="stylesheet">
<style>
:root{
  --orange:#f37122;
  --yellow:#ffc214;
  --green:#acd136;
  --blue:#3276b5;
  --soft-blue:#85acd3;
  --pale:#e3eef8;
  --ink:#1a1a1a;
  --text:#555;
  --footer:#000;
  --footer-text:#ddd;
}
*{margin:0;padding:0;box-sizing:border-box}
html,body{width:759px;height:1200px;overflow:hidden;background:#fff}
body{position:relative;font-family:"Mulish",sans-serif;color:var(--text)}
.abs{position:absolute}
h2,h3,.nav,.btn,.hero-text{font-family:"Montserrat",sans-serif}

/* header */
.brand{left:46px;top:12px;display:flex;align-items:center;gap:8px}
.brand-dot{width:72px;height:72px;border-radius:50%;background:var(--blue)}
.brand-name{font-family:"Montserrat",sans-serif;font-weight:600;font-size:11px;color:var(--blue);width:120px;line-height:1.3}
.social{display:flex;gap:3px}
.social span{width:24px;height:24px;display:block}
.social-top{left:638px;top:11px}
.help{left:471px;top:55px;display:flex;align-items:center;gap:8px}
.help small{display:block;font-size:7px;font-weight:600;color:#333;font-family:"Montserrat",sans-serif}
.help b{display:block;font-size:12px;font-weight:500;color:#222;font-family:"Montserrat",sans-serif}
.auth{left:596px;top:56px;display:flex;gap:3px}
.auth span{height:20px;width:57px;display:flex;align-items:center;justify-content:center;color:#fff;font-size:7.5px;font-family:"Montserrat",sans-serif;font-weight:500}

.nav{left:0;top:99px;width:759px;height:24px;background:var(--orange);display:flex;align-items:center;padding-left:66px}
.nav a{color:#fff;font-size:7.5px;font-weight:500;text-decoration:none;margin-right:25.5px}

/* hero */
.hero{left:0;top:123px;width:759px;height:367px;background:linear-gradient(100deg,#2f5f94 0%,#6c8fb5 35%,#d9d2c8 62%,#7a5a48 85%,#3a5b86 100%)}
.hero-line{left:0;top:489px;width:759px;height:2px;background:var(--soft-blue)}
.hero-text{left:87px;top:211px;color:#111}
.hero-text .k1{font-size:19.5px;font-weight:500;letter-spacing:.2px}
.hero-text .k2{font-size:39px;font-weight:600;line-height:1.05}
.hero-text .k3{font-size:13.5px;font-weight:400;margin-top:5px}
.arrow{width:31px;height:31px;border-radius:50%;background:rgba(255,255,255,.85);display:flex;align-items:center;justify-content:center}

/* about */
h2{font-weight:500;color:var(--ink);font-size:17.5px}
.sub{font-size:10px;color:#333;margin-top:4px}
.about{left:46px;top:518px;width:425px}
.about p{font-size:8.6px;line-height:15.2px;margin-top:12px}
.btn{display:inline-flex;align-items:center;justify-content:center;color:#fff;font-size:7.8px;font-weight:500;height:21px}
.divider{left:483px;top:500px;width:6px;height:226px;background:linear-gradient(90deg,rgba(0,0,0,.05),rgba(0,0,0,0))}
.testi{left:502px;top:518px;width:215px}
.quote{left:502px;top:566px;font-family:Georgia,serif;font-size:32px;color:var(--orange);font-weight:bold}
.testi p{font-size:8.6px;line-height:15.2px;margin:12px 0 0 28px}
.author{left:502px;top:664px;display:flex;align-items:center;gap:8px}
.avatar{width:40px;height:40px;border-radius:50%;background:linear-gradient(#d8b9a2,#a57c62);border:2px solid #eee}
.author .n{color:var(--orange);font-size:10px}
.author .r{font-size:9px;color:#333;margin-left:6px}

/* courses */
.band{left:0;top:727px;width:759px;height:279px;background:var(--pale)}
.courses{left:47px;top:758px}
.list{left:47px;top:806px;display:grid;grid-template-columns:171px 150px}
.list li{list-style:none;font-size:8.7px;color:#444;height:20px;display:flex;align-items:center}
.list li::before{content:"›";color:#888;font-size:9px;margin-right:6px}
.team{left:388px;top:758px}
.team-img{left:388px;top:808px;width:325px;height:163px;border:3px solid #fff;background:linear-gradient(180deg,#dfe6ee 0%,#9ab9da 55%,#3a7bbf 100%)}

/* footer */
.top-btn{left:359px;top:992px;width:27px;height:27px;border-radius:50%;background:#000;border:2px solid #fff;display:flex;align-items:center;justify-content:center;z-index:2}
.footer{left:0;top:1006px;width:759px;height:164px;background:var(--footer)}
.col{top:1032px;color:#fff}
.col h3{font-size:10.5px;font-weight:400;margin-bottom:8px;color:#fff}
.col li{list-style:none;font-size:7.8px;line-height:14px;color:var(--footer-text)}
.col.tight li{line-height:11.7px}
.col p{font-size:7.8px;line-height:11.7px;color:var(--footer-text)}
.news{left:445px;top:1034px;color:#fff}
.news-head{display:flex;gap:9px;align-items:center}
.news-head b{font-size:10px;font-weight:600;font-family:"Montserrat",sans-serif;color:#fff}
.news-head small{display:block;font-size:7.5px;color:var(--footer-text);margin-top:2px}
.field{width:189px;height:23px;background:#fff;font-size:7.5px;color:#999;padding:0 8px;display:flex;align-items:center}
.subscribe{left:663px;top:1073px;width:49px;height:52px;background:var(--green);flex-direction:column;color:#111;font-size:7px;font-weight:600}

.copy{left:46px;top:1180px;font-size:7.8px;color:#444}
.social-bottom{left:638px;top:1172px}
.social-bottom span{background:#cfcfcf}
</style>
</head>
<body>

<header>
  <div class="abs brand"><span class="brand-dot"></span><span class="brand-name">Guidance in Calm Posture Support Methods</span></div>
  <div class="abs social social-top"><span style="background:#2aa9e0"></span><span style="background:#0e76a8"></span><span style="background:#3db54a"></span></div>
  <div class="abs help">
    <svg width="20" height="20" viewBox="0 0 24 24" fill="none" stroke="#888" stroke-width="1.4"><path d="M5 3l4 1 1 4-2 2a12 12 0 0 0 6 6l2-2 4 1 1 4-3 2C10 21 3 14 3 6z"/></svg>
    <div><small>NEED TO HELP!</small><b>1800 555 0142</b></div>
  </div>
  <div class="abs auth"><span style="background:var(--green)">LOGIN</span><span style="background:var(--yellow)">REGISTER</span></div>
</header>

<nav class="abs nav">
  <a>INTRODUCTION</a><a>TOBACCO PRODUCTS</a><a>NICOTINE ADDICTION</a><a>BRIEF INTERVENTIONS</a><a>CASE SCENARIOS</a><a>RESOURCES</a><a>CONTACT</a>
</nav>

<section>
  <div class="abs hero" role="img" aria-label="Photo of a smiling healthcare provider with a stethoscope in front of her clinical team, with a no-smoking symbol"></div>
  <div class="abs hero-text">
    <div class="k1">BRIEF CLINICAL INTERVENTIONS</div>
    <div class="k2">FOR TOBACCO USE</div>
    <div class="k3">TIPS FOR BUSY HEALTHCARE PROVIDERS</div>
  </div>
  <div class="abs arrow" style="left:46px;top:292px"><svg width="10" height="12" viewBox="0 0 10 12"><path d="M7 1L2 6l5 5" stroke="#333" stroke-width="2" fill="none"/></svg></div>
  <div class="abs arrow" style="left:681px;top:292px"><svg width="10" height="12" viewBox="0 0 10 12"><path d="M3 1l5 5-5 5" stroke="#333" stroke-width="2" fill="none"/></svg></div>
  <div class="abs hero-line"></div>
</section>

<section>
  <div class="abs about">
    <h2>Guidance in Calm Posture Support Methods</h2>
    <div class="sub">About our company information</div>
    <p>Lorem ipsum dolor sit amet, consectetuer adipiscing elit, sed diam nonummy nibh euismod tincidunt ut laoreet dolore magna aliquam erat volutpat. Ut wisi enim ad minim veniam, quis nostrud exerci tation ullamcorper suscipit lobortis nisl ut aliquip ex ea commodo consequat. Duis autem vel eum iriure dolor in hendrerit in vulputate velit esse molestie consequat, vel illum dolore eu feugiat nulla facilisis at vero eros et accumsan et iusto odio dignissim qui blandit praesent luptatum zzril delenit augue duis dolore te feugait nulla facilisi. Nam liber tempor cum soluta nobis eleifend option congue nihil imperdiet doming id quod mazim placerat facer possim assum.</p>
  </div>
  <span class="abs btn" style="left:46px;top:683px;width:69px;background:var(--soft-blue)">LEARN MORE</span>
  <div class="abs divider"></div>
  <div class="abs testi">
    <h2>Testimonials</h2>
    <div class="sub">What people say about me</div>
    <p>Lorem ipsum dolor sit amet, consectetuer adipiscing elit, sed diam nonummy nibh euismod tincidunt ut laoreet dolore magna aliquam erat volutpat. Ut wisi enim ad minim ullamcorper suscipit lobortis nisl ut aliquip ex ea commodo consequat.</p>
  </div>
  <div class="abs quote">“</div>
  <div class="abs author">
    <div class="avatar" role="img" aria-label="Portrait of the reviewer"></div>
    <div><div class="n">- Mara Ellison</div><div class="r">commodo consequat</div></div>
  </div>
</section>

<section>
  <div class="abs band"></div>
  <div class="abs courses"><h2>E-Learning Courses</h2><div class="sub">Our latest e-learning healthcare courses</div></div>
  <ul class="abs list">
    <li>Lorem ipsum dolor sit amet</li><li>Lorem ipsum dolor sit amet</li>
    <li>Lorem ipsum dolor sit amet</li><li>Lorem ipsum dolor sit amet</li>
    <li>Lorem ipsum dolor sit amet</li><li>Lorem ipsum dolor sit amet</li>
    <li>Lorem ipsum dolor sit amet</li><li>Lorem ipsum dolor sit amet</li>
    <li>Lorem ipsum dolor sit amet</li><li>Lorem ipsum dolor sit amet</li>
    <li>Lorem ipsum dolor sit amet</li><li>Lorem ipsum dolor sit amet</li>
    <li>Lorem ipsum dolor sit amet</li><li>Lorem ipsum dolor sit amet</li>
  </ul>
  <span class="abs btn" style="left:47px;top:950px;width:160px;background:var(--orange)">LEARN MORE E-LEARNING COURSES</span>
  <div class="abs team"><h2>Our Team</h2><div class="sub">Clinical Tobacco Intervention Program for clinical professionals</div></div>
  <div class="abs team-img" role="img" aria-label="Photo of a smiling team of doctors and nurses with arms crossed"></div>
</section>

<footer>
  <div class="abs top-btn"><svg width="12" height="12" viewBox="0 0 12 12"><circle cx="6" cy="6" r="5.3" stroke="#fff" fill="none"/><path d="M3.5 7.2L6 4.7l2.5 2.5" stroke="#fff" stroke-width="1.3" fill="none"/></svg></div>
  <div class="abs footer"></div>
  <div class="abs col" style="left:46px"><h3>Quick links</h3><ul><li>Introduction</li><li>Tobacco Products</li><li>Nicotine Addiction</li><li>Brief Interventions</li><li>Case Scenarios</li><li>Resources</li><li>Contact</li></ul></div>
  <div class="abs col" style="left:160px"><h3>Contact Info</h3>
    <p>Guidance in Calm Posture Support Methods<br>14 Willow Court,<br>Avon Park 30412</p>
    <p style="margin-top:12px">T: 1800 555 0142<br>F: 1800 555 01<br>E:info@calmposture.org<br>W:www.calmposture.org</p>
  </div>
  <div class="abs col tight" style="left:331px"><h3>Other Links</h3><ul><li>E-Learning</li><li>About Us</li><li>FAQ</li><li>Testimonials</li><li>Resources</li><li>Privacy Policy</li><li>Terms of Us</li><li>Sitemap</li></ul></div>
  <div class="abs news">
    <div class="news-head">
      <svg width="38" height="26" viewBox="0 0 38 26" fill="none" stroke="#fff" stroke-width="1.3"><path d="M12 6l20-4 4 18-20 4z"/><path d="M12 6l13 8 11-12"/><path d="M0 12h9M2 16h8M4 20h9"/></svg>
      <div><b>Subscribe Our Newsletter - Today!</b><small>Enter your name and email &amp; receive latest news &amp; offers!!!</small></div>
    </div>
  </div>
  <div class="abs field" style="left:445px;top:1073px">Enter your name</div>
  <div class="abs field" style="left:445px;top:1102px">Enter your email</div>
  <span class="abs btn subscribe"><svg width="14" height="12" viewBox="0 0 14 12"><path d="M0 6l14-6-4 12-3-4z" fill="#111"/></svg><span style="margin-top:4px">SUBSCRIBE</span></span>

  <div class="abs copy">Copyright © 2016 Guidance in Calm Posture Support Methods. All Rights Reserved</div>
  <div class="abs social social-bottom"><span></span><span></span><span></span></div>
</footer>

</body>
</html>
```